Velvet Harbor (A luxury Travel Website)

website text attached in document below

images also attached

feel free to use other images if needed

Target Market(s)

Luxury Seekers and wealthy couples / families

Industry/Entity Type

Luxury Travel

Coding

Coded - Design and coding required

Number of Pages Required

1 page

Requirements
Must have
• A luxury design and easy use.
Nice to have
• Ease of use of page, incorporation of images into the flow of the site

```html
<!DOCTYPE html>
<html lang="en">
<head>
<meta charset="utf-8">
<title>Velvet Harbor – Luxury Travel</title>
<link href="https://fonts.googleapis.com/css2?family=Federant&family=Oswald:wght@400&family=Barlow:wght@400;500;600&display=swap" rel="stylesheet">
<style>
:root{
  --ink:#111111;
  --black:#000000;
  --white:#ffffff;
  --accent:#17b1d3;
  --accent-dark:#1a7fb4;
  --panel:#eef9fc;
  --line:#d9dde2;
  --muted:#555a60;
  --footer:#14100f;
}
*{box-sizing:border-box;margin:0;padding:0}
html,body{width:1200px;height:2999px;overflow:hidden;background:var(--white)}
body{position:relative;font-family:"Barlow",sans-serif;color:var(--ink)}
.abs{position:absolute}
.display{font-family:"Federant",serif}

/* header */
.site-header{left:0;top:0;width:1200px;height:75px;background:var(--black);color:var(--white)}
.header-phone{left:163px;top:26px;font-size:14px;display:flex;align-items:center;gap:8px}
.brand{font-family:"Barlow",sans-serif;font-weight:500;letter-spacing:3px;text-transform:uppercase;color:var(--white)}
.header-brand{left:0;width:1200px;top:22px;text-align:center;font-size:26px}
.book-btn{left:940px;top:22px;width:97px;height:29px;border:1px solid var(--accent);color:var(--white);font-size:14px;display:flex;align-items:center;justify-content:center}

/* hero */
.hero{left:0;top:75px;width:1200px;height:600px}
.hero-title{left:0;width:1200px;top:300px;text-align:center;color:var(--white);font-size:41px;line-height:49px;text-shadow:0 2px 8px rgba(0,0,0,.4)}
.hero-sub{left:0;width:1200px;top:408px;text-align:center;color:var(--white);font-family:"Oswald",sans-serif;font-size:25px;text-shadow:0 2px 6px rgba(0,0,0,.4)}
.btn{background:var(--accent);color:var(--white);font-weight:500;display:flex;align-items:center;justify-content:center}
.hero-btn{left:509px;top:474px;width:182px;height:49px;font-size:18px;letter-spacing:.5px}

/* quick quote card */
.quote-card{left:162px;top:725px;width:876px;height:203px;background:var(--white);box-shadow:0 4px 16px rgba(0,0,0,.09)}
.quote-text{left:100px;top:54px;font-size:23px;line-height:32px;letter-spacing:.5px}
.quote-divider{left:467px;top:50px;width:1px;height:105px;background:#eceff2}
.field{border:1px solid var(--line);background:var(--white);display:flex;align-items:center;gap:10px;padding-left:12px;font-size:12px;color:#333}
.quote-email{left:506px;top:60px;width:273px;height:41px}
.quote-upload{left:518px;top:122px;font-size:12px;display:flex;align-items:center;gap:10px;color:#333}
.quote-submit{left:682px;top:110px;width:97px;height:41px;font-size:18px}

/* holiday form */
.holiday-photo{left:162px;top:1020px;width:442px;height:592px;background:linear-gradient(180deg,#3f8bd0 0%,#6aa7d8 25%,#556b3c 45%,#b5682c 65%,#2a3f63 85%,#1b2a48 100%)}
.holiday-accent{left:680px;top:1164px;width:364px;height:359px;border-right:6px solid var(--accent);border-bottom:6px solid var(--accent)}
.holiday-panel{left:520px;top:1103px;width:518px;height:414px;background:var(--panel)}
.holiday-title{left:0;width:518px;top:60px;text-align:center;font-size:22px;line-height:30px}
.holiday-panel .field{height:37px;font-size:12px;gap:8px}
.holiday-submit{left:210px;top:309px;width:106px;height:44px;font-size:18px}

/* gallery */
.gallery-tile{top:1702px;width:210px;height:312px}

/* hotels */
.section-title{left:0;width:1200px;top:2106px;text-align:center;font-size:44px}
.hotel-card{top:2202px;width:285px;height:367px;background:var(--white);box-shadow:0 3px 10px rgba(0,0,0,.08)}
.hotel-photo{left:0;top:0;width:100%;height:285px}
.hotel-name{left:0;width:100%;top:298px;text-align:center;font-size:21px;font-weight:500;line-height:28px}
.slider-arrow{top:2299px;width:34px;height:34px;border-radius:50%;background:var(--white);box-shadow:0 2px 8px rgba(0,0,0,.1);display:flex;align-items:center;justify-content:center}

/* footer */
.site-footer{left:0;top:2660px;width:1200px;height:339px;background:linear-gradient(180deg,#1c1714 0%,#2a1f18 45%,#120e0c 100%)}
.footer-brand{left:0;width:1200px;top:56px;text-align:center;font-size:36px}
.contact{width:300px;top:146px;text-align:center;color:var(--white)}
.contact-label{color:var(--accent);font-weight:600;font-size:16px;margin-top:12px}
.contact-value{font-size:13px;margin-top:2px}
.footer-rule{left:162px;top:285px;width:876px;height:1px;background:rgba(255,255,255,.3)}
.copyright{left:0;width:1200px;top:303px;text-align:center;color:var(--white);font-size:14px}
</style>
</head>
<body>

<header class="abs site-header">
  <div class="abs header-phone">
    <svg width="14" height="14" viewBox="0 0 24 24"><path fill="#fff" d="M6.6 10.8a15.1 15.1 0 0 0 6.6 6.6l2.2-2.2c.3-.3.7-.4 1-.2 1.1.4 2.3.6 3.6.6.6 0 1 .4 1 1V20c0 .6-.4 1-1 1A17 17 0 0 1 3 4c0-.6.4-1 1-1h3.5c.6 0 1 .4 1 1 0 1.3.2 2.5.6 3.6.1.3 0 .7-.2 1z"/></svg>
    <span>+61 2 5550 1842</span>
  </div>
  <div class="abs brand header-brand">Velvet Harbor</div>
  <div class="abs book-btn">Book Now</div>
</header>

<section class="abs hero">
  <svg class="abs" style="left:0;top:0" width="1200" height="600" viewBox="0 0 1200 600">
    <defs>
      <linearGradient id="heroTone" x1="0" y1="0" x2="1" y2="1">
        <stop offset="0" stop-color="#6b4a40"/>
        <stop offset=".4" stop-color="#b99b86"/>
        <stop offset=".7" stop-color="#5a4038"/>
        <stop offset="1" stop-color="#2b1e22"/>
      </linearGradient>
      <linearGradient id="swoosh" x1="0" y1="0" x2="1" y2="0">
        <stop offset="0" stop-color="#1a5fa8"/>
        <stop offset="1" stop-color="#17b1d3"/>
      </linearGradient>
    </defs>
    <path role="img" aria-label="Traveller relaxing in a business class seat" d="M0 0H1200V415C1000 520 700 580 400 590C200 596 60 560 0 470Z" fill="url(#heroTone)"/>
    <path d="M0 470C60 560 200 596 400 590C700 580 1000 520 1200 415V405C1000 505 700 565 400 578C210 584 70 550 0 455Z" fill="url(#swoosh)"/>
  </svg>
  <h1 class="abs display hero-title">Looking To Stay At A 5 Star Hotel Or To<br>Fly Business Class Anywhere?</h1>
  <p class="abs hero-sub">Share A Screenshot Of Your Travel Plans And We Beat The Price, Within 24 Hours.</p>
  <div class="abs btn hero-btn">CONTACT US</div>
</section>

<section class="abs quote-card">
  <p class="abs display quote-text">We Work Directly With Hotels<br>&amp; Airlines To Get You The<br>Best Price,always.</p>
  <div class="abs quote-divider"></div>
  <div class="abs field quote-email">
    <svg width="16" height="12" viewBox="0 0 16 12"><rect x="0.5" y="0.5" width="15" height="11" fill="none" stroke="#17b1d3"/><path d="M1 1l7 6 7-6" fill="none" stroke="#17b1d3"/></svg>
    <span>Email Address</span>
  </div>
  <div class="abs quote-upload">
    <svg width="18" height="16" viewBox="0 0 18 16"><rect x="1" y="1" width="16" height="14" fill="none" stroke="#17b1d3"/><path d="M3 12l4-5 3 3 2-2 3 4" fill="none" stroke="#17b1d3"/></svg>
    <span>Upload Screenshot</span>
  </div>
  <div class="abs btn quote-submit">Submit</div>
</section>

<section>
  <div class="abs holiday-photo" role="img" aria-label="Resort villa with palm trees and pool at dusk"></div>
  <div class="abs holiday-accent"></div>
  <div class="abs holiday-panel">
    <h2 class="abs display holiday-title">Tell Us About Your Next Holiday Plans.<br>The More Details The Better.</h2>
    <div class="abs field" style="left:20px;top:139px;width:239px">
      <svg width="12" height="12" viewBox="0 0 12 12"><circle cx="6" cy="3.5" r="3" fill="#17b1d3"/><path d="M0 12c0-4 3-5 6-5s6 1 6 5z" fill="#17b1d3"/></svg><span>Your Name*</span></div>
    <div class="abs field" style="left:266px;top:139px;width:238px">
      <svg width="14" height="10" viewBox="0 0 16 12"><rect x="0.5" y="0.5" width="15" height="11" fill="none" stroke="#17b1d3"/><path d="M1 1l7 6 7-6" fill="none" stroke="#17b1d3"/></svg><span>Your Email*</span></div>
    <div class="abs field" style="left:20px;top:190px;width:239px">
      <svg width="12" height="12" viewBox="0 0 24 24"><path fill="#17b1d3" d="M6.6 10.8a15.1 15.1 0 0 0 6.6 6.6l2.2-2.2c.3-.3.7-.4 1-.2 1.1.4 2.3.6 3.6.6.6 0 1 .4 1 1V20c0 .6-.4 1-1 1A17 17 0 0 1 3 4c0-.6.4-1 1-1h3.5c.6 0 1 .4 1 1 0 1.3.2 2.5.6 3.6.1.3 0 .7-.2 1z"/></svg><span>Phone*</span></div>
    <div class="abs field" style="left:266px;top:190px;width:238px">
      <svg width="12" height="12" viewBox="0 0 12 12"><rect x="0.5" y="1.5" width="11" height="10" fill="none" stroke="#17b1d3"/><rect x="0.5" y="1.5" width="11" height="3" fill="#17b1d3"/></svg><span>Date*</span></div>
    <div class="abs field" style="left:20px;top:241px;width:113px">
      <svg width="14" height="12" viewBox="0 0 14 12"><circle cx="4" cy="3" r="2.5" fill="#17b1d3"/><circle cx="10" cy="3" r="2.5" fill="#17b1d3"/><path d="M0 12c0-3 2-4 4-4s4 1 4 4zM6 12c0-3 2-4 4-4s4 1 4 4z" fill="#17b1d3"/></svg><span>Adult*</span></div>
    <div class="abs field" style="left:141px;top:241px;width:119px">
      <svg width="13" height="12" viewBox="0 0 13 12"><circle cx="6.5" cy="6" r="5.5" fill="none" stroke="#17b1d3"/><circle cx="4.5" cy="5" r="1" fill="#17b1d3"/><circle cx="8.5" cy="5" r="1" fill="#17b1d3"/></svg><span>Child*</span></div>
    <div class="abs field" style="left:266px;top:241px;width:238px">
      <svg width="10" height="13" viewBox="0 0 10 13"><path d="M5 13S0 7.5 0 5a5 5 0 0 1 10 0c0 2.5-5 8-5 8z" fill="#17b1d3"/><circle cx="5" cy="5" r="2" fill="#fff"/></svg><span>Destination*</span></div>
    <div class="abs btn holiday-submit">Submit</div>
  </div>
</section>

<section>
  <div class="abs gallery-tile" style="left:162px;background:linear-gradient(160deg,#3b4a44,#55b9b0 45%,#7fd3c8 65%,#4a5a58)" role="img" aria-label="Aerial view of overwater villas around a lagoon"></div>
  <div class="abs gallery-tile" style="left:384px;background:linear-gradient(180deg,#2f5fa8,#4a7cc0 30%,#a0553a 55%,#5a3a2a 75%,#243a3c)" role="img" aria-label="Resort lodge reflected in an infinity pool"></div>
  <div class="abs gallery-tile" style="left:606px;background:linear-gradient(150deg,#2fb4c8,#5fd0de 40%,#6b4a36 60%,#2aa8c0)" role="img" aria-label="Overwater villa with private pool"></div>
  <div class="abs gallery-tile" style="left:830px;background:linear-gradient(180deg,#2c5f9e,#5b8fc4 35%,#3f6b4a 50%,#6fd4d2 70%,#4dc4c8)" role="img" aria-label="Island resort with a long jetty of water villas"></div>
</section>

<section>
  <h2 class="abs display section-title">Best 5 Star Hotels</h2>
  <div class="abs slider-arrow" style="left:61px">
    <svg width="8" height="8" viewBox="0 0 8 8"><path d="M5.5 1L2.5 4l3 3" fill="none" stroke="#17b1d3" stroke-width="1.2"/></svg></div>
  <div class="abs slider-arrow" style="left:1102px">
    <svg width="8" height="8" viewBox="0 0 8 8"><path d="M2.5 1l3 3-3 3" fill="none" stroke="#17b1d3" stroke-width="1.2"/></svg></div>

  <article class="abs hotel-card" style="left:162px">
    <div class="abs hotel-photo" style="background:linear-gradient(160deg,#1e5f8e,#2f9bb8 45%,#6fd0d4 65%,#1f6c94)" role="img" aria-label="Aerial view of a curved row of overwater villas"></div>
    <h3 class="abs hotel-name">Coralwind Spa<br>Island</h3>
  </article>
  <article class="abs hotel-card" style="left:459px">
    <div class="abs hotel-photo" style="background:linear-gradient(180deg,#c9b8a8,#9cc3c8 30%,#3cb8c4 55%,#1f8da8)" role="img" aria-label="Overwater pavilion and jetty in a turquoise lagoon"></div>
    <h3 class="abs hotel-name">The Lagoon House, Azure<br>Atoll</h3>
  </article>
  <article class="abs hotel-card" style="left:754px">
    <div class="abs hotel-photo" style="background:linear-gradient(170deg,#8eb4d8,#3f9fc4 35%,#e6e0cf 55%,#4b7a4a 75%,#2f9fb8)" role="img" aria-label="Beachfront resort on a white sand island"></div>
    <h3 class="abs hotel-name">Palm Crest Resort<br>Sandbar Isle</h3>
  </article>
</section>

<footer class="abs site-footer">
  <div class="abs brand footer-brand">Velvet Harbor</div>

  <div class="abs contact" style="left:100px">
    <svg width="26" height="42" viewBox="0 0 26 42"><rect x="1" y="1" width="24" height="40" rx="3" fill="none" stroke="#fff" stroke-width="1.5"/><line x1="1" y1="7" x2="25" y2="7" stroke="#fff" stroke-width="1.5"/><line x1="1" y1="33" x2="25" y2="33" stroke="#fff" stroke-width="1.5"/><circle cx="13" cy="37" r="1.6" fill="#fff"/></svg>
    <div class="contact-label">Phone</div>
    <div class="contact-value">+61 2 5550 1842</div>
  </div>
  <div class="abs contact" style="left:422px">
    <svg width="30" height="42" viewBox="0 0 30 42"><path d="M15 41S1.5 24 1.5 14.5a13.5 13.5 0 0 1 27 0C28.5 24 15 41 15 41z" fill="none" stroke="#fff" stroke-width="1.5"/><circle cx="15" cy="14.5" r="5" fill="none" stroke="#fff" stroke-width="1.5"/></svg>
    <div class="contact-label">Address</div>
    <div class="contact-value">14 Quay Lane, Sydney</div>
  </div>
  <div class="abs contact" style="left:771px">
    <svg width="42" height="34" viewBox="0 0 42 34"><rect x="1" y="1" width="40" height="32" fill="none" stroke="#fff" stroke-width="1.5"/><path d="M1 1l20 18L41 1M1 33l15-15M41 33L26 18" fill="none" stroke="#fff" stroke-width="1.5"/></svg>
    <div class="contact-label">Email</div>
    <div class="contact-value">hello@velvetharbor.travel</div>
  </div>

  <div class="abs footer-rule"></div>
  <p class="abs copyright">© 2022 Velvet Harbor. All Rights Reserved.</p>
</footer>

</body>
</html>
```